Korvell Plant Services

We are a heavy diesel mechanical business with additional air con certificates, remapping engine rebuilt

Contact Information for Business Card

Company Name, Director Name, Managing Director, Contact details, email and website

Font styles to use
Serif
Script

```html
<!DOCTYPE html>
<html lang="en">
<head>
<meta charset="utf-8">
<title>Korvell Plant Services – Business Card</title>
<link href="https://fonts.googleapis.com/css2?family=Great+Vibes&family=Libre+Baskerville:wght@400;700&display=swap" rel="stylesheet">
<style>
  :root {
    --navy: #2b2a78;
    --navy-deep: #1e1d5c;
    --navy-tone: #3a3996;
    --ink: #17171c;
    --paper: #f1f1f3;
    --grey-text: #55555e;
    --stage: #d9dae2;
    --serif: "Libre Baskerville", serif;
    --script: "Great Vibes", cursive;
  }
  * { margin: 0; padding: 0; box-sizing: border-box; }
  html, body { width: 1200px; height: 800px; overflow: hidden; }
  body {
    background: var(--stage);
    font-family: var(--serif);
    display: flex;
    align-items: center;
    justify-content: center;
    gap: 44px;
  }
  .card {
    position: relative;
    width: 540px;
    height: 309px;
    overflow: hidden;
    box-shadow: 0 10px 28px rgba(20, 20, 60, 0.22);
  }
  .card-front svg.card-shape { position: absolute; inset: 0; }
  .card-front .details {
    position: absolute;
    left: 122px;
    top: 40px;
    color: var(--grey-text);
  }
  .person-name {
    font-family: var(--script);
    color: var(--navy);
    font-weight: 400;
    font-size: 34px;
    line-height: 1.1;
  }
  .person-role {
    font-size: 13px;
    margin-top: 2px;
    letter-spacing: 0.02em;
  }
  .address {
    font-size: 11.5px;
    line-height: 1.45;
    margin-top: 14px;
  }
  .contact-list {
    list-style: none;
    font-size: 11.5px;
    line-height: 1.5;
  }
  .contact-list li { display: flex; align-items: center; gap: 6px; }
  .contact-list svg { width: 11px; height: 11px; fill: var(--navy); flex: none; }
  .front-brand {
    position: absolute;
    right: 30px;
    bottom: 28px;
    display: flex;
    align-items: center;
    gap: 8px;
    color: var(--navy);
    font-weight: 700;
    font-size: 15px;
  }
  .brand-dot {
    width: 13px; height: 13px;
    border-radius: 50%;
    background: var(--navy);
    flex: none;
  }
  .card-back {
    background: linear-gradient(135deg, var(--navy-tone) 0%, var(--navy) 50%, var(--navy-deep) 100%);
  }
  .back-brand {
    position: absolute;
    inset: 0;
    display: flex;
    align-items: center;
    justify-content: center;
    gap: 14px;
    color: #4846a8;
    font-weight: 700;
    font-size: 27px;
  }
  .back-brand .brand-dot { width: 24px; height: 24px; background: #4846a8; }
</style>
</head>
<body>
  <section class="card card-front" aria-label="Business card front">
    <svg class="card-shape" viewBox="0 0 540 309" width="540" height="309" aria-hidden="true">
      <rect width="540" height="309" fill="var(--navy)"/>
      <circle cx="374" cy="154" r="306" fill="var(--paper)"/>
      <circle cx="378" cy="154" r="303" fill="var(--ink)"/>
      <circle cx="386" cy="154" r="300" fill="var(--paper)"/>
    </svg>
    <div class="details">
      <h1 class="person-name">Dane R. Ashworth</h1>
      <p class="person-role">Managing Director</p>
      <p class="address">Korvell Plant Services<br>48 Quarry Lane<br>Unit 3 Ashby, MA 01431</p>
      <ul class="contact-list">
        <li><svg viewBox="0 0 24 24"><path d="M6.6 10.8a15 15 0 0 0 6.6 6.6l2.2-2.2c.3-.3.7-.4 1-.2 1.1.4 2.3.6 3.6.6.6 0 1 .4 1 1V20c0 .6-.4 1-1 1A17 17 0 0 1 3 4c0-.6.4-1 1-1h3.5c.6 0 1 .4 1 1 0 1.3.2 2.5.6 3.6.1.3 0 .7-.2 1z"/></svg>(555) 014-2290</li>
        <li><svg viewBox="0 0 24 24"><path d="M2 5h20v14H2zm2 2v.5l8 5 8-5V7zm0 2.8V17h16V9.8l-8 5z"/></svg>info@korvellplant.com</li>
        <li><svg viewBox="0 0 24 24"><path d="M12 2a10 10 0 1 0 0 20 10 10 0 0 0 0-20zm6.9 6h-3a15 15 0 0 0-1.3-3.9A8 8 0 0 1 18.9 8zM12 4c.8 1.2 1.5 2.5 1.9 4h-3.8c.4-1.5 1.1-2.8 1.9-4zM4.3 14a8 8 0 0 1 0-4h3.4a16 16 0 0 0 0 4zm.8 2h3a15 15 0 0 0 1.3 3.9A8 8 0 0 1 5.1 16zm3-8h-3a8 8 0 0 1 4.3-3.9A15 15 0 0 0 8.1 8zM12 20c-.8-1.2-1.5-2.5-1.9-4h3.8c-.4 1.5-1.1 2.8-1.9 4zm2.3-6H9.7a14 14 0 0 1 0-4h4.6a14 14 0 0 1 0 4zm.3 5.9a15 15 0 0 0 1.3-3.9h3a8 8 0 0 1-4.3 3.9zm1.7-5.9a16 16 0 0 0 0-4h3.4a8 8 0 0 1 0 4z"/></svg>www.korvellplant.com</li>
      </ul>
    </div>
    <div class="front-brand"><span class="brand-dot"></span>Korvell Plant Services</div>
  </section>

  <section class="card card-back" aria-label="Business card back">
    <div class="back-brand"><span class="brand-dot"></span>Korvell Plant Services</div>
  </section>
</body>
</html>
```